Willowbend Pharmacy Business Cards

I need a business card design and or template. Needs to convey a softer feel along with health and wellness. Please see attached logo and color scheme.

Industry/Entity Type

Pharmacy

Colors

Designer to choose colors to be used in the design.

Requirements
Must have
• I've added a second NEW colored logo I think I am going to go with the blue green logo.
• Needs to have the colors and feel of the logo attached.
• Darrel Quimby
• Pharmacy Manager
• willowbendpharmacy.example

```html
<!DOCTYPE html>
<html lang="en">
<head>
<meta charset="utf-8">
<title>Willowbend Pharmacy Business Cards</title>
<link href="https://fonts.googleapis.com/css2?family=Open+Sans:wght@400;600;700&display=swap" rel="stylesheet">
<style>
  :root {
    --backdrop: #6e4c36;
    --leaf-green: #a3c945;
    --sky-blue: #2ea3dc;
    --charcoal: #232323;
    --white: #ffffff;
    --ink-line: #111111;
  }
  * { margin: 0; padding: 0; box-sizing: border-box; }
  html, body { width: 1200px; height: 1000px; overflow: hidden; }
  body {
    background: var(--backdrop);
    font-family: "Open Sans", Arial, sans-serif;
    position: relative;
  }
  .card {
    position: absolute;
    left: 267px;
    width: 665px;
    height: 396px;
    border-radius: 22px;
    overflow: hidden;
  }
  .card--front { top: 74px; background: var(--leaf-green); }
  .card--back { top: 534px; background: var(--charcoal); }

  .brand {
    position: absolute;
    display: flex;
    align-items: center;
    gap: 14px;
    font-weight: 600;
    white-space: nowrap;
    letter-spacing: -0.3px;
  }
  .brand__dot { border-radius: 50%; flex: none; }
  .card--front .brand {
    left: 118px; top: 168px;
    font-size: 42px; color: var(--white);
  }
  .card--front .brand__dot { width: 40px; height: 40px; background: var(--white); }
  .card--back .brand {
    right: 32px; top: 76px;
    font-size: 34px; color: var(--white);
  }
  .card--back .brand__dot { width: 34px; height: 34px; background: var(--sky-blue); }

  .holder { position: absolute; left: 32px; top: 196px; }
  .holder__name {
    color: var(--sky-blue); font-weight: 700; font-size: 21px; line-height: 26px;
  }
  .holder__title { color: var(--white); font-size: 16px; line-height: 22px; }

  .contact {
    position: absolute; left: 334px; top: 189px;
    color: var(--white); font-size: 16px; line-height: 21px;
  }
  .contact__address { margin-bottom: 6px; }
  .contact__row { display: flex; align-items: center; gap: 7px; margin-bottom: 1px; }
  .contact__icon { width: 14px; height: 14px; flex: none; }

  .wave { position: absolute; left: 0; bottom: 0; width: 665px; height: 120px; }
</style>
</head>
<body>
  <section class="card card--front" aria-label="Card front">
    <div class="brand"><span class="brand__dot"></span>Willowbend Pharmacy</div>
  </section>

  <section class="card card--back" aria-label="Card back">
    <div class="brand"><span class="brand__dot"></span>Willowbend Pharmacy</div>

    <div class="holder">
      <p class="holder__name">DARREL QUIMBY</p>
      <p class="holder__title">Pharmacy Manager</p>
    </div>

    <div class="contact">
      <p class="contact__address">418 Larchmere Avenue, Suite 12<br>Fernbrook Ontario K2P</p>
      <p class="contact__row">
        <svg class="contact__icon" viewBox="0 0 16 16"><path fill="#a3c945" d="M1 6c0-2 3-4 7-4s7 2 7 4l-3 1-1-2H5L4 7 1 6zm3 2h8l2 6H2l2-6zm4 1a2 2 0 100 4 2 2 0 000-4z"/></svg>
        555-014-2271 ext. 140
      </p>
      <p class="contact__row">
        <svg class="contact__icon" viewBox="0 0 16 16"><rect x="1" y="3" width="14" height="10" fill="#a3c945"/><path d="M1 3l7 6 7-6" fill="none" stroke="#232323" stroke-width="1.4"/></svg>
        Darrel@willowbendpharmacy.example
      </p>
      <p class="contact__row">
        <svg class="contact__icon" viewBox="0 0 16 16"><circle cx="8" cy="8" r="6.5" fill="none" stroke="#a3c945" stroke-width="2"/><path d="M1.5 8h13M8 1.5c-3 3-3 10 0 13M8 1.5c3 3 3 10 0 13" fill="none" stroke="#a3c945" stroke-width="1.3"/></svg>
        www.willowbendpharmacy.example
      </p>
    </div>

    <svg class="wave" viewBox="0 0 665 120" preserveAspectRatio="none" aria-hidden="true">
      <path fill="var(--leaf-green)" d="M0 60 C60 30 140 18 230 30 C330 44 380 96 470 96 C560 96 620 60 665 36 L665 120 L0 120 Z"/>
      <path fill="var(--ink-line)" d="M90 22 C200 2 300 30 380 60 C440 82 500 92 560 78 C610 66 645 46 665 34 C630 58 580 86 510 92 C430 98 380 74 320 50 C250 24 180 14 90 22 Z"/>
      <path fill="var(--sky-blue)" d="M90 20 C200 -2 300 20 380 48 C440 70 500 80 560 68 C610 58 645 40 665 28 C630 50 580 76 510 82 C430 88 380 66 320 44 C250 20 180 12 90 20 Z"/>
    </svg>
  </section>
</body>
</html>
```